Ideation to Execution

Create a graphic illustrating the iterative interaction between Design Thinking's Investment Readiness Levels (IRL), Technical Readiness Levels (TRL), and New Product Introduction Execution. Showcase a hybrid approach, integrating Stage-Gate processes with Agile iteration loops, highlighting how these elements interact in a continuous feedback loop to refine and advance product development from concept to market readiness.

```html
<!DOCTYPE html>
<html lang="en">
<head>
<meta charset="utf-8">
<title>Lean Innovation, NTI, and NPI</title>
<link href="https://fonts.googleapis.com/css2?family=Roboto:wght@300;400;500;700;900&family=Roboto+Condensed:wght@300;700&family=Source+Sans+3:wght@400&display=swap" rel="stylesheet">
<style>
:root{
  --page:#e8e8e8;
  --white:#ffffff;
  --ink:#111111;
  --yellow:#fdb913;
  --yellow-mid:#fdca45;
  --yellow-light:#fedc7a;
  --band:#d9d9d9;
  --divider:#ececec;
  --pill:#a3a3a3;
  --dark-grey:#595959;
  --mid-grey:#7f7f7f;
  --light-grey:#b3b3b3;
  --footer-ink:#7a5a10;
}
*{margin:0;padding:0;box-sizing:border-box}
html,body{width:1021px;height:1200px;overflow:hidden;background:var(--page)}
body{position:relative;font-family:"Roboto",sans-serif;color:var(--ink)}
.slide{position:absolute;left:75px;width:1505px;height:847px;background:var(--white);transform:scale(.5787);transform-origin:0 0;box-shadow:0 3px 8px rgba(0,0,0,.18);overflow:hidden}
.slide-a{top:83px}
.slide-b{top:627px}
.abs{position:absolute}
.c{position:absolute;transform:translate(-50%,-50%);text-align:center;white-space:nowrap}
.title{position:absolute;left:0;right:0;top:14px;text-align:center;font-weight:900;font-size:49px;letter-spacing:-.5px}
.title-mark{position:absolute;left:734px;top:78px;width:77px;height:28px;background:var(--yellow);clip-path:polygon(0 0,100% 0,50% 100%)}
.divider{position:absolute;left:0;right:0;background:linear-gradient(180deg,var(--divider),#f6f6f6)}
.rule{position:absolute;left:23px;width:1446px;height:1.5px;background:#8c8c8c}
.chev{position:absolute;overflow:visible}
.icon{position:absolute;border-radius:10px;background:linear-gradient(135deg,#e9e9e9,#cfcfcf);border:2px solid #333}
.icon.warn{background:linear-gradient(135deg,#f2f2f2 55%,var(--yellow) 55%)}
.search{position:absolute;left:125px;line-height:1}
.search .lead{font-weight:700;font-size:22px;display:block}
.search .risk{font-weight:900;font-size:27px;display:block;margin-top:4px;line-height:27px}
.label-back{position:absolute;background:linear-gradient(90deg,rgba(240,240,240,0),#eeeeee);clip-path:polygon(0 0,calc(100% - 16px) 0,100% 50%,calc(100% - 16px) 100%,0 100%)}
.side-label{position:absolute;text-align:right;font-weight:700;font-size:19px;line-height:23px;transform:translateY(-50%)}
.band{position:absolute;background:var(--band);clip-path:polygon(0 0,calc(100% - 22px) 0,100% 50%,calc(100% - 22px) 100%,0 100%,18px 50%)}
.stage{position:absolute;transform:translate(-50%,-50%);text-align:center;font-size:14px;line-height:15px;white-space:nowrap;color:#222}
.stage.bold{font-weight:700;font-size:16px;line-height:18px;color:var(--ink)}
.step{position:absolute;transform:translate(-50%,-50%);font-size:15px;white-space:nowrap;color:#222}
.dot{position:absolute;width:15px;height:15px;border-radius:50%;background:var(--ink);transform:translate(-50%,-50%)}
.dot::after{content:"";position:absolute;left:4px;top:4.5px;width:4px;height:4px;border-right:1.6px solid var(--white);border-top:1.6px solid var(--white);transform:rotate(45deg)}
.pill{position:absolute;height:20px;min-width:40px;padding:0 8px;border-radius:10px;background:var(--pill);color:var(--white);font-weight:700;font-size:11px;line-height:20px;text-align:center;transform:translate(-50%,-50%);box-shadow:inset 0 -2px 0 rgba(0,0,0,.12)}
.pill.wide{min-width:60px}
.pill::before{content:"";position:absolute;left:50%;top:-12px;width:1px;height:12px;background:#9a9a9a}
.tail{position:absolute;width:1px;background:#9a9a9a}
.readiness{position:absolute;font-weight:700;font-size:14px;transform:translateY(-50%);white-space:nowrap}
.irl{position:absolute;font-weight:700;font-size:18px;transform:translateY(-50%)}
.card{position:absolute;width:269px;background:var(--white);box-shadow:0 2px 6px rgba(0,0,0,.12)}
.card-head{height:54px;display:flex;align-items:center;padding-left:16px;gap:14px;font-weight:700;font-size:19px;color:var(--white)}
.card-head .glyph{width:34px;height:34px;border-radius:6px;border:2px solid currentColor;opacity:.8}
.card-head.problem{background:var(--yellow);color:var(--ink)}
.card-head.solution{background:var(--ink)}
.card-head.model{background:var(--mid-grey)}
.card-body{height:71px;padding:14px 0 0 22px;font-size:18px;font-weight:300;line-height:24px;color:#222}
.next{position:absolute;width:34px;height:34px;border-radius:50%;background:var(--ink);transform:translate(-50%,-50%);z-index:2}
.next::after{content:"";position:absolute;left:11px;top:12px;width:8px;height:8px;border-right:2.5px solid var(--white);border-top:2.5px solid var(--white);transform:rotate(45deg)}
.validated{position:absolute;font-size:14px;line-height:17px;color:#222}
.arrow-block{position:absolute;height:156px;display:flex;flex-direction:column;align-items:center;justify-content:center;text-align:center;color:var(--white);clip-path:polygon(0 0,calc(100% - 26px) 0,100% 50%,calc(100% - 26px) 100%,0 100%,22px 50%)}
.arrow-block h3{font-weight:700;font-size:23px}
.arrow-block .dash{width:38px;height:2px;background:currentColor;margin:11px 0 12px}
.arrow-block p{font-size:18px;font-weight:300;line-height:24px}
.arrow-block.problem{background:var(--yellow);color:var(--ink)}
.arrow-block.solution{background:var(--ink)}
.arrow-block.model{background:linear-gradient(90deg,var(--dark-grey) 0 55%,var(--light-grey) 55%)}
.execute{position:absolute;left:125px;font-weight:900;font-size:27px;transform:translateY(-50%)}
.group{position:absolute;left:0;width:1505px}
.brand-line{position:absolute;left:17px;top:778px;font-family:"Roboto Condensed",sans-serif;font-weight:300;font-size:30px;color:var(--yellow)}
.wordmark{position:absolute;right:22px;top:771px;font-weight:900;font-size:27px;letter-spacing:-.5px;color:var(--ink)}
.footer-bar{position:absolute;left:0;right:0;top:816px;height:31px;background:linear-gradient(100deg,var(--yellow) 0 63.5%,var(--yellow-mid) 63.5% 86%,var(--yellow-light) 86%)}
.classification{position:absolute;left:0;top:828px;font-family:"Source Sans 3",sans-serif;font-size:13px;color:var(--footer-ink)}
.page-no{position:absolute;right:10px;top:833px;font-size:10px;color:var(--footer-ink)}
</style>
</head>
<body>

<!-- Slide one: card layout -->
<section class="slide slide-a">
  <h1 class="title">LEAN INNOVATION, NTI, AND NPI</h1>
  <div class="title-mark"></div>

  <div class="divider" style="top:128px;height:5px"></div>
  <div class="divider" style="top:320px;height:16px"></div>
  <div class="divider" style="top:492px;height:14px"></div>

  <!-- Market risk row -->
  <div class="icon warn" role="img" aria-label="Market risk icon: chart screen with warning sign" style="left:21px;top:194px;width:80px;height:67px"></div>
  <div class="search" style="top:190px"><span class="lead">Search:</span><span class="risk">Address<br>Market Risk</span></div>
  <div class="label-back" style="left:300px;top:150px;width:116px;height:126px"></div>
  <div class="side-label" style="right:1113px;top:218px">Lean<br>Innovation</div>

  <div class="card" style="left:422px;top:151px">
    <div class="card-head problem"><span class="glyph" role="img" aria-label="Problem icon"></span>PROBLEM</div>
    <div class="card-body">Identify new<br>customer needs</div>
  </div>
  <div class="next" style="left:700px;top:237px"></div>
  <div class="card" style="left:710px;top:151px">
    <div class="card-head solution"><span class="glyph" role="img" aria-label="Solution icon"></span>SOLUTION</div>
    <div class="card-body">Test solution ideas<br>with customers</div>
  </div>
  <div class="next" style="left:988px;top:237px"></div>
  <div class="card" style="left:998px;top:151px">
    <div class="card-head model"><span class="glyph" role="img" aria-label="Business model icon"></span>BUSINESS MODEL</div>
    <div class="card-body">Is it a big growth idea?<br>Is it sustainable?</div>
  </div>
  <div class="validated" style="left:1289px;top:216px">Validated Customer Need<br>Validated Solution Desirability<br>Validated Willingness to Pay</div>

  <div class="irl" style="left:353px;top:297px">IRL</div>
  <span class="pill" style="left:422px;top:302px">0</span>
  <span class="pill" style="left:476px;top:302px">1</span>
  <span class="pill" style="left:521px;top:302px">2</span>
  <span class="pill" style="left:711px;top:302px">3</span>
  <span class="pill" style="left:768px;top:302px">4</span>
  <span class="pill" style="left:999px;top:302px">5</span>
  <span class="pill" style="left:1054px;top:302px">6</span>
  <span class="pill" style="left:1118px;top:302px">7</span>
  <span class="pill" style="left:1188px;top:302px">8</span>
  <span class="pill" style="left:1263px;top:302px">9</span>

  <svg class="chev" style="left:138px;top:311px" width="76" height="38" viewBox="0 0 76 38"><polyline points="4,4 38,32 72,4" fill="none" stroke="#fdb913" stroke-width="9"/></svg>

  <!-- Technical risk row -->
  <div class="group" style="top:367px">
    <div class="icon warn" role="img" aria-label="Technical risk icon: gear with warning sign" style="left:26px;top:9px;width:73px;height:70px;border-radius:50%"></div>
    <div class="search" style="top:8px"><span class="lead">Search:</span><span class="risk">Address<br>Technical Risk</span></div>
    <div class="label-back" style="left:330px;top:0;width:160px;height:69px"></div>
    <div class="side-label" style="right:1025px;top:34px">NTI Process</div>
    <div class="band" style="left:484px;top:0;width:982px;height:69px"></div>
    <div class="stage bold" style="left:561px;top:34px">Practical<br>Application</div>
    <span class="dot" style="left:630px;top:35px"></span><div class="stage" style="left:678px;top:35px">Concept<br>Evaluation</div>
    <span class="dot" style="left:731px;top:35px"></span><div class="stage" style="left:775px;top:35px">Concept<br>Demo</div>
    <span class="dot" style="left:822px;top:35px"></span><div class="stage" style="left:868px;top:35px">Concept<br>Demo</div>
    <span class="dot" style="left:912px;top:35px"></span><div class="stage" style="left:966px;top:35px">Concept<br>Verification</div>
    <span class="dot" style="left:1019px;top:35px"></span><div class="stage" style="left:1074px;top:35px">Production<br>Prototype<br>Evaluation</div>
    <span class="dot" style="left:1130px;top:35px"></span><div class="stage" style="left:1184px;top:35px">Production<br>Pilot<br>Validation</div>
    <span class="dot" style="left:1238px;top:35px"></span><div class="stage" style="left:1300px;top:35px">Initial<br>Development/<br>Production</div>
    <span class="dot" style="left:1361px;top:35px"></span><div class="stage" style="left:1411px;top:35px">TRL<br>Production<br>Review</div>
    <div class="readiness" style="left:348px;top:91px">Technology Readiness Level (TRL)</div>
    <span class="pill wide" style="left:629px;top:89px">TRL 0</span>
    <span class="pill wide" style="left:731px;top:89px">TRL 1</span>
    <span class="pill wide" style="left:822px;top:89px">TRL 2</span>
    <span class="pill wide" style="left:912px;top:89px">TRL 3</span>
    <span class="pill wide" style="left:1019px;top:89px">TRL 4</span>
    <span class="pill wide" style="left:1130px;top:89px">TRL 5</span>
    <span class="pill wide" style="left:1240px;top:89px">TRL 6</span>
    <span class="pill wide" style="left:1361px;top:89px">TRL 7</span>
    <span class="pill wide" style="left:1461px;top:89px">TRL 8</span>
  </div>

  <svg class="chev" style="left:138px;top:483px" width="76" height="38" viewBox="0 0 76 38"><polyline points="4,4 38,32 72,4" fill="none" stroke="#fdb913" stroke-width="9"/></svg>

  <!-- Execute rows -->
  <div class="icon" role="img" aria-label="Execute icon: gear with check mark" style="left:34px;top:596px;width:74px;height:73px;border-radius:50%;background:radial-gradient(circle,var(--yellow) 0 22%,#f2f2f2 23%)"></div>
  <div class="execute" style="top:631px">Execute</div>

  <div class="group" style="top:527px">
    <div class="label-back" style="left:590px;top:0;width:225px;height:69px"></div>
    <div class="side-label" style="right:694px;top:34px">Full NPI</div>
    <div class="band" style="left:815px;top:0;width:650px;height:69px"></div>
    <div class="stage bold" style="left:891px;top:35px">Program<br>Strategy</div>
    <span class="dot" style="left:960px;top:36px"></span><div class="step" style="left:1008px;top:36px">Concept</div>
    <span class="dot" style="left:1067px;top:36px"></span><div class="step" style="left:1130px;top:36px">Develop</div>
    <span class="dot" style="left:1191px;top:36px"></span><div class="step" style="left:1245px;top:36px">Pilot</div>
    <span class="dot" style="left:1298px;top:36px"></span><div class="step" style="left:1360px;top:36px">Production</div>
    <div class="tail" style="left:1465px;top:34px;height:44px"></div>
    <span class="pill" style="left:960px;top:88px">L</span>
    <span class="pill" style="left:1005px;top:88px">1</span>
    <span class="pill" style="left:1052px;top:88px">2</span>
    <span class="pill" style="left:1102px;top:88px">3</span>
    <span class="pill" style="left:1146px;top:88px">4</span>
    <span class="pill" style="left:1190px;top:88px">5</span>
    <span class="pill" style="left:1244px;top:88px">PCR</span>
    <span class="pill" style="left:1297px;top:88px">6</span>
    <span class="pill" style="left:1465px;top:88px">7</span>

    <div class="label-back" style="left:590px;top:112px;width:225px;height:69px"></div>
    <div class="side-label" style="right:694px;top:146px">Accelerated NPI</div>
    <div class="band" style="left:815px;top:112px;width:615px;height:69px"></div>
    <div class="stage bold" style="left:891px;top:147px">Program<br>Plan</div>
    <span class="dot" style="left:960px;top:148px"></span><div class="step" style="left:1008px;top:148px">Concept</div>
    <span class="dot" style="left:1067px;top:148px"></span><div class="step" style="left:1130px;top:148px">Develop</div>
    <span class="dot" style="left:1191px;top:148px"></span><div class="step" style="left:1245px;top:148px">Pilot</div>
    <span class="dot" style="left:1298px;top:148px"></span><div class="step" style="left:1360px;top:148px">Production</div>
    <div class="tail" style="left:1428px;top:146px;height:44px"></div>
    <span class="pill" style="left:960px;top:199px">1</span>
    <span class="pill" style="left:1102px;top:199px">3</span>
    <span class="pill" style="left:1190px;top:199px">5</span>
    <span class="pill" style="left:1297px;top:199px">6</span>
    <span class="pill" style="left:1428px;top:199px">7</span>
  </div>

  <div class="brand-line">IRONWORKS LEAN INNOVATION</div>
  <div class="wordmark">IRONWORKS</div>
  <div class="footer-bar"></div>
  <div class="classification">Ironworks: Confidential Green</div>
  <div class="page-no">1</div>
</section>

<!-- Slide two: arrow layout -->
<section class="slide slide-b">
  <h1 class="title">LEAN INNOVATION, NTI, AND NPI</h1>
  <div class="title-mark"></div>

  <!-- Market risk row -->
  <div class="icon warn" role="img" aria-label="Market risk icon: chart screen with warning sign" style="left:21px;top:205px;width:80px;height:67px"></div>
  <div class="search" style="top:200px"><span class="lead">Search:</span><span class="risk">Address<br>Market Risk</span></div>
  <div class="label-back" style="left:310px;top:157px;width:130px;height:156px"></div>
  <div class="side-label" style="right:1092px;top:235px">Lean<br>Innovation</div>

  <div class="arrow-block problem" style="left:420px;top:157px;width:296px"><h3>PROBLEM</h3><span class="dash"></span><p>Identify new<br>customer needs</p></div>
  <div class="arrow-block solution" style="left:698px;top:157px;width:295px"><h3>SOLUTION</h3><span class="dash"></span><p>Test solution ideas<br>with customers</p></div>
  <div class="arrow-block model" style="left:975px;top:157px;width:295px"><h3>BUSINESS MODEL</h3><span class="dash"></span><p>Is it a big growth idea?<br>Is it sustainable?</p></div>
  <div class="tail" style="left:1266px;top:270px;height:56px"></div>
  <div class="validated" style="left:1289px;top:214px">Validated Customer Need<br>Validated Solution Desirability<br>Validated Willingness to Pay</div>

  <div class="irl" style="left:377px;top:337px">IRL</div>
  <span class="pill" style="left:447px;top:337px">0</span>
  <span class="pill" style="left:502px;top:337px">1</span>
  <span class="pill" style="left:546px;top:337px">2</span>
  <span class="pill" style="left:736px;top:337px">3</span>
  <span class="pill" style="left:793px;top:337px">4</span>
  <span class="pill" style="left:1002px;top:337px">5</span>
  <span class="pill" style="left:1056px;top:337px">6</span>
  <span class="pill" style="left:1120px;top:337px">7</span>
  <span class="pill" style="left:1190px;top:337px">8</span>
  <span class="pill" style="left:1266px;top:337px">9</span>

  <div class="rule" style="top:368px"></div>
  <svg class="chev" style="left:143px;top:360px" width="46" height="24" viewBox="0 0 46 24"><polyline points="3,3 23,19 43,3" fill="none" stroke="#fdb913" stroke-width="6"/></svg>

  <!-- Technical risk row -->
  <div class="group" style="top:395px">
    <div class="icon warn" role="img" aria-label="Technical risk icon: gear with warning sign" style="left:26px;top:9px;width:73px;height:70px;border-radius:50%"></div>
    <div class="search" style="top:9px"><span class="lead">Search:</span><span class="risk">Address<br>Technical Risk</span></div>
    <div class="label-back" style="left:330px;top:0;width:160px;height:69px"></div>
    <div class="side-label" style="right:1025px;top:34px">NTI Process</div>
    <div class="band" style="left:484px;top:0;width:982px;height:69px"></div>
    <div class="stage bold" style="left:561px;top:34px">Practical<br>Application</div>
    <span class="dot" style="left:630px;top:35px"></span><div class="stage" style="left:678px;top:35px">Concept<br>Evaluation</div>
    <span class="dot" style="left:731px;top:35px"></span><div class="stage" style="left:775px;top:35px">Concept<br>Demo</div>
    <span class="dot" style="left:822px;top:35px"></span><div class="stage" style="left:868px;top:35px">Concept<br>Demo</div>
    <span class="dot" style="left:912px;top:35px"></span><div class="stage" style="left:966px;top:35px">Concept<br>Verification</div>
    <span class="dot" style="left:1019px;top:35px"></span><div class="stage" style="left:1074px;top:35px">Production<br>Prototype<br>Evaluation</div>
    <span class="dot" style="left:1130px;top:35px"></span><div class="stage" style="left:1184px;top:35px">Production<br>Pilot<br>Validation</div>
    <span class="dot" style="left:1238px;top:35px"></span><div class="stage" style="left:1300px;top:35px">Initial<br>Development/<br>Production</div>
    <span class="dot" style="left:1361px;top:35px"></span><div class="stage" style="left:1411px;top:35px">TRL<br>Production<br>Review</div>
    <div class="readiness" style="left:348px;top:91px">Technology Readiness Level (TRL)</div>
    <span class="pill wide" style="left:629px;top:89px">TRL 0</span>
    <span class="pill wide" style="left:731px;top:89px">TRL 1</span>
    <span class="pill wide" style="left:822px;top:89px">TRL 2</span>
    <span class="pill wide" style="left:912px;top:89px">TRL 3</span>
    <span class="pill wide" style="left:1019px;top:89px">TRL 4</span>
    <span class="pill wide" style="left:1130px;top:89px">TRL 5</span>
    <span class="pill wide" style="left:1240px;top:89px">TRL 6</span>
    <span class="pill wide" style="left:1361px;top:89px">TRL 7</span>
    <span class="pill wide" style="left:1461px;top:89px">TRL 8</span>
  </div>

  <div class="rule" style="top:516px"></div>
  <svg class="chev" style="left:143px;top:507px" width="46" height="24" viewBox="0 0 46 24"><polyline points="3,3 23,19 43,3" fill="none" stroke="#fdb913" stroke-width="6"/></svg>

  <!-- Execute rows -->
  <div class="icon" role="img" aria-label="Execute icon: gear with check mark" style="left:34px;top:577px;width:74px;height:73px;border-radius:50%;background:radial-gradient(circle,var(--yellow) 0 22%,#f2f2f2 23%)"></div>
  <div class="execute" style="top:612px">Execute</div>

  <div class="group" style="top:531px">
    <div class="label-back" style="left:590px;top:0;width:225px;height:69px"></div>
    <div class="side-label" style="right:694px;top:34px">Full NPI</div>
    <div class="band" style="left:815px;top:0;width:650px;height:69px"></div>
    <div class="stage bold" style="left:891px;top:35px">Program<br>Strategy</div>
    <span class="dot" style="left:960px;top:36px"></span><div class="step" style="left:1008px;top:36px">Concept</div>
    <span class="dot" style="left:1067px;top:36px"></span><div class="step" style="left:1130px;top:36px">Develop</div>
    <span class="dot" style="left:1191px;top:36px"></span><div class="step" style="left:1245px;top:36px">Pilot</div>
    <span class="dot" style="left:1298px;top:36px"></span><div class="step" style="left:1360px;top:36px">Production</div>
    <div class="tail" style="left:1465px;top:34px;height:44px"></div>
    <span class="pill" style="left:960px;top:87px">L</span>
    <span class="pill" style="left:1005px;top:87px">1</span>
    <span class="pill" style="left:1052px;top:87px">2</span>
    <span class="pill" style="left:1102px;top:87px">3</span>
    <span class="pill" style="left:1146px;top:87px">4</span>
    <span class="pill" style="left:1190px;top:87px">5</span>
    <span class="pill" style="left:1244px;top:87px">PCR</span>
    <span class="pill" style="left:1297px;top:87px">6</span>
    <span class="pill" style="left:1465px;top:87px">7</span>

    <div class="label-back" style="left:590px;top:112px;width:225px;height:69px"></div>
    <div class="side-label" style="right:694px;top:146px">Accelerated NPI</div>
    <div class="band" style="left:815px;top:112px;width:615px;height:69px"></div>
    <div class="stage bold" style="left:891px;top:147px">Program<br>Plan</div>
    <span class="dot" style="left:960px;top:148px"></span><div class="step" style="left:1008px;top:148px">Concept</div>
    <span class="dot" style="left:1067px;top:148px"></span><div class="step" style="left:1130px;top:148px">Develop</div>
    <span class="dot" style="left:1191px;top:148px"></span><div class="step" style="left:1245px;top:148px">Pilot</div>
    <span class="dot" style="left:1298px;top:148px"></span><div class="step" style="left:1360px;top:148px">Production</div>
    <div class="tail" style="left:1428px;top:146px;height:44px"></div>
    <span class="pill" style="left:960px;top:199px">1</span>
    <span class="pill" style="left:1102px;top:199px">3</span>
    <span class="pill" style="left:1190px;top:199px">5</span>
    <span class="pill" style="left:1297px;top:199px">6</span>
    <span class="pill" style="left:1428px;top:199px">7</span>
  </div>

  <div class="brand-line">IRONWORKS LEAN INNOVATION</div>
  <div class="wordmark">IRONWORKS</div>
  <div class="footer-bar"></div>
  <div class="classification">Ironworks: Confidential Green</div>
  <div class="page-no">2</div>
</section>

</body>
</html>
```